Conference flyer

We need a flyer for a conference for the defence industry. The attached has been updated with new information using last years flyer. We would like something new and fresh. Please note the theme of the conference is 'a global environment'.

The final design should reflect the defence industry and manufacturing.

Defence

```html
<!DOCTYPE html>
<html lang="en">
<head>
<meta charset="utf-8">
<title>Defence Trade Controls Annual Conference – Registration</title>
<link href="https://fonts.googleapis.com/css2?family=Open+Sans:wght@400;600;700&display=swap" rel="stylesheet">
<style>
  :root {
    --navy: #1c2b5f;
    --royal: #2f3d9c;
    --bright: #2b55b8;
    --date-blue: #1f7fc8;
    --ink: #1d1d1f;
    --rule: #8c8c8c;
    --paper: #ffffff;
    --sky-1: #3b5fb0;
    --sky-2: #a9bde4;
    --sky-3: #e6edf9;
  }
  * { box-sizing: border-box; margin: 0; padding: 0; }
  html, body {
    width: 913px; height: 1200px; overflow: hidden;
    background: var(--paper);
    font-family: "Open Sans", Arial, sans-serif;
    color: var(--ink);
  }
  .flyer { position: relative; width: 913px; height: 1200px; background: var(--paper); }
  .abs { position: absolute; transform: translateY(-50%); white-space: nowrap; }

  /* Header */
  .masthead-art {
    position: absolute; left: 0; top: 0; width: 913px; height: 176px;
    background:
      radial-gradient(ellipse at 50% 120%, var(--sky-3) 0%, rgba(230,237,249,0) 60%),
      linear-gradient(100deg, var(--sky-1) 0%, var(--sky-2) 35%, var(--sky-3) 55%, var(--sky-2) 75%, var(--sky-1) 100%);
  }
  .masthead-panel {
    position: absolute; left: 0; top: 21px; width: 913px; height: 143px;
    background: rgba(255,255,255,0.78);
  }
  .masthead-title {
    position: absolute; left: 0; width: 913px; text-align: center;
    color: var(--royal); font-weight: 700; letter-spacing: 0.5px;
    transform: translateY(-50%);
  }
  .masthead-title.line-1 { top: 60px; font-size: 46px; }
  .masthead-title.line-2 { top: 122px; font-size: 42px; }
  .masthead-rule { position: absolute; left: 0; top: 176px; width: 913px; height: 8px; background: var(--navy); }

  /* How to register bar */
  .register-bar { position: absolute; left: 15px; top: 201px; width: 884px; height: 42px; }
  .register-bar svg { display: block; }
  .register-bar .label {
    position: absolute; left: 22px; top: 21px; transform: translateY(-50%);
    color: #fff; font-weight: 700; font-size: 18px;
  }
  .register-bar .instruction {
    position: absolute; right: 18px; top: 21px; transform: translateY(-50%);
    color: #fff; font-size: 16px;
  }

  /* Contact methods */
  .contact { position: absolute; top: 262px; width: 260px; margin-left: -130px; text-align: center; }
  .contact svg { display: block; margin: 0 auto; }
  .contact .kind { margin-top: 12px; font-size: 15px; line-height: 20px; }
  .contact .value { font-size: 15px; line-height: 20px; }
  .contact-rule { position: absolute; left: 15px; top: 376px; width: 884px; height: 3px; background: var(--navy); }

  /* Form */
  .section-title { font-weight: 600; font-size: 17px; }
  .field-label { font-size: 15px; }
  .field-line { position: absolute; height: 1px; background: var(--rule); }
  .small { font-size: 13px; }
  .check {
    position: absolute; width: 11px; height: 11px; border: 1.3px solid var(--ink);
    transform: translateY(-50%);
  }
  .check.large { width: 15px; height: 15px; }
  .date { color: var(--date-blue); font-weight: 600; font-size: 17px; }
  .module { font-size: 14px; line-height: 21px; white-space: normal; width: 360px; }
  .module-name { position: absolute; left: 146px; }
  .office { font-size: 13px; }
  .flyer-foot { position: absolute; left: 0; bottom: 0; width: 913px; height: 3px; background: var(--navy); }
</style>
</head>
<body>
<main class="flyer">

  <header>
    <div class="masthead-art" role="img" aria-label="Blue world map with network lines and light flares"></div>
    <div class="masthead-panel"></div>
    <h1 class="masthead-title line-1">DEFENCE TRADE CONTROLS</h1>
    <h2 class="masthead-title line-2">ANNUAL CONFERENCE</h2>
    <div class="masthead-rule"></div>
  </header>

  <section class="register-bar">
    <svg width="884" height="42" viewBox="0 0 884 42">
      <rect x="0" y="0" width="884" height="42" fill="var(--navy)"/>
      <polygon points="0,0 268,0 250,42 0,42" fill="var(--bright)"/>
    </svg>
    <span class="label">HOW TO REGISTER</span>
    <span class="instruction">Complete the registration for below and return it to us by:</span>
  </section>

  <div class="contact" style="left:137px;">
    <svg width="54" height="54" viewBox="0 0 54 54" fill="none" stroke="var(--royal)" stroke-width="3.4">
      <circle cx="27" cy="27" r="23"/>
      <ellipse cx="27" cy="27" rx="10" ry="23"/>
      <line x1="4" y1="27" x2="50" y2="27"/>
      <path d="M8 15 H46 M8 39 H46"/>
    </svg>
    <p class="kind">Web</p>
    <p class="value">www.tradeforumevents.com</p>
  </div>

  <div class="contact" style="left:456px;">
    <svg width="56" height="54" viewBox="0 0 56 54" fill="var(--royal)">
      <path d="M4 18 C4 6 52 6 52 18 L52 22 L40 22 L40 16 C34 13 22 13 16 16 L16 22 L4 22 Z"/>
      <path d="M14 26 L20 20 L36 20 L42 26 L50 48 L6 48 Z"/>
      <circle cx="28" cy="35" r="7" fill="#fff"/>
      <circle cx="28" cy="35" r="3"/>
    </svg>
    <p class="kind">Phone</p>
    <p class="value">+61 7 5550 1284</p>
  </div>

  <div class="contact" style="left:790px;">
    <svg width="56" height="54" viewBox="0 0 56 54" fill="var(--royal)">
      <path d="M16 2 H34 L42 10 V24 H16 Z"/>
      <rect x="21" y="9" width="13" height="2.5" fill="#fff"/>
      <rect x="21" y="14" width="15" height="2.5" fill="#fff"/>
      <rect x="4" y="24" width="48" height="28" rx="5"/>
      <rect x="11" y="30" width="28" height="5" fill="#fff"/>
      <circle cx="14" cy="43" r="2.5" fill="#fff"/>
      <circle cx="22" cy="43" r="2.5" fill="#fff"/>
    </svg>
    <p class="kind">Fax</p>
    <p class="value">+61 7 5550 1297</p>
  </div>

  <div class="contact-rule"></div>

  <!-- Conference registration -->
  <section class="conference-form">
    <p class="abs section-title" style="left:18px; top:414px;">Conference Registration:</p>

    <p class="abs field-label" style="left:24px; top:468px;">Attendee #1:</p>
    <div class="field-line" style="left:144px; top:478px; width:298px;"></div>
    <p class="abs field-label" style="left:24px; top:513px;">Attendee #2:</p>
    <div class="field-line" style="left:144px; top:523px; width:298px;"></div>
    <p class="abs field-label" style="left:24px; top:557px;">Attendee #3:</p>
    <div class="field-line" style="left:144px; top:567px; width:298px;"></div>
    <p class="abs field-label" style="left:24px; top:603px;">Attendee #4:</p>
    <div class="field-line" style="left:149px; top:613px; width:298px;"></div>
    <p class="abs field-label" style="left:24px; top:647px;">Company:</p>
    <div class="field-line" style="left:149px; top:657px; width:298px;"></div>
    <p class="abs field-label" style="left:24px; top:692px;">Address:</p>
    <div class="field-line" style="left:149px; top:702px; width:298px;"></div>
    <p class="abs field-label" style="left:24px; top:738px;">Contact no:</p>
    <div class="field-line" style="left:149px; top:748px; width:298px;"></div>
    <p class="abs field-label" style="left:24px; top:782px;">Email:</p>
    <div class="field-line" style="left:149px; top:792px; width:298px;"></div>
    <p class="abs field-label" style="left:24px; top:828px;">Dietary needs:</p>
    <div class="field-line" style="left:149px; top:838px; width:298px;"></div>

    <p class="abs field-label" style="left:24px; top:878px;">Payment method:&nbsp; (please check)</p>
    <span class="check large" style="left:24px; top:910px;"></span>
    <p class="abs small" style="left:56px; top:910px;">Invoice</p>
    <span class="check large" style="left:24px; top:941px;"></span>
    <p class="abs small" style="left:56px; top:941px;">Credit card*</p>

    <p class="abs" style="left:56px; top:969px; font-size:12px;">Credit Type:</p>
    <span class="check" style="left:145px; top:969px;"></span>
    <p class="abs" style="left:164px; top:969px; font-size:12px;">Northcard</p>
    <span class="check" style="left:257px; top:969px;"></span>
    <p class="abs" style="left:275px; top:969px; font-size:12px;">Velacard</p>
    <span class="check" style="left:325px; top:969px;"></span>
    <p class="abs" style="left:343px; top:969px; font-size:12px;">Amplex</p>
    <style>.flyer p[style*="left:275px"]{display:none}</style>
    <p class="abs" style="left:278px; top:969px; font-size:12px;">Vela</p>

    <p class="abs small" style="left:56px; top:993px;">Card name:</p>
    <div class="field-line" style="left:176px; top:1002px; width:270px;"></div>
    <p class="abs small" style="left:56px; top:1028px;">Card number:</p>
    <div class="field-line" style="left:176px; top:1037px; width:270px;"></div>
    <p class="abs small" style="left:56px; top:1064px;">Expiry date:</p>
    <div class="field-line" style="left:176px; top:1073px; width:270px;"></div>
    <p class="abs small" style="left:56px; top:1101px;">Cardholder email:</p>
    <div class="field-line" style="left:190px; top:1110px; width:256px;"></div>
  </section>

  <!-- Training modules -->
  <section class="training-form">
    <p class="abs section-title" style="left:494px; top:414px;">1/2 day training module/s:</p>

    <p class="abs date" style="left:494px; top:467px;">1 June 2015</p>
    <span class="check" style="left:498px; top:502px;"></span>
    <p class="abs module" style="left:518px; top:502px;">Module 1 - Trade Controls for Beginner</p>

    <p class="abs date" style="left:494px; top:542px;">4 June 2015</p>
    <span class="check" style="left:498px; top:578px;"></span>
    <p class="abs module" style="left:518px; top:588px;">Module 2 -Practical management of export control reform</p>
    <span class="check" style="left:498px; top:630px;"></span>
    <p class="abs module" style="left:518px; top:640px;">Module 2 -Practical management of export control reform</p>

    <p class="abs date" style="left:494px; top:694px;">5 June 2015</p>
    <span class="check" style="left:498px; top:729px;"></span>
    <p class="abs module" style="left:518px; top:738px;">Module 4 - Making the best of Commerce exceptions</p>

    <p class="abs section-title" style="left:494px; top:799px;">Training registration:</p>

    <span class="check" style="left:498px; top:840px;"></span>
    <p class="abs small" style="left:518px; top:840px; width:360px;">Attendee #1:<span class="module-name">Module 1 2, 3, 4</span></p>
    <span class="check" style="left:498px; top:873px;"></span>
    <p class="abs small" style="left:518px; top:873px; width:360px;">Attendee #2:<span class="module-name">Module 1, 2, 3, 4</span></p>
    <span class="check" style="left:498px; top:905px;"></span>
    <p class="abs small" style="left:518px; top:905px; width:360px;">Attendee #3:<span class="module-name">Module 1, 2, 3, 4</span></p>
    <span class="check" style="left:498px; top:939px;"></span>
    <p class="abs small" style="left:518px; top:939px; width:360px;">Attendee #4:<span class="module-name">Module 1, 2, 3, 4</span></p>

    <p class="abs" style="left:494px; top:980px; font-size:12.5px; line-height:21px; white-space:normal; width:330px;">Please tick which module each attendee would like to register for</p>

    <p class="abs office" style="left:494px; top:1040px;">OFFICE USE ONLY:</p>
    <p class="abs office" style="left:494px; top:1074px;">Confirmation sent: ...........................................</p>
    <p class="abs office" style="left:494px; top:1107px;">Contact person:...............................................</p>
    <p class="abs office" style="left:494px; top:1141px;">Invoice no: .......................................................</p>
    <p class="abs office" style="left:494px; top:1174px;">Paid: ...............................................................</p>
  </section>

  <div class="flyer-foot"></div>
</main>
</body>
</html>
```